Exciting product design for natural pet treats

We need a design for our stand up doy style pouch that blends well with our current logo and also bold enough to stand out from the crowd.

We have a range of natural, Australian made pet treats and need a generic bag that allows for a sticker to be placed on the bag to idenfity the name, while also allowing a space for another sticker on the back for ingredients.
___
Information for the front is: logo, Australian made and owned, Pet Food Only (this is a small font and should not be hero text), 100% Natural, Visit our web site for more amazing products for your pets, Space for sticker 100 - 150mm x 30mm.
___
Information for the back is: Kibblo Nest is proudly Australian owned and operated. We source all our Kibblo Nest treats from reputable suppliers around Australia.

Our Kibblo Nest treats can be purchased through our online store, where you will find a growing range of other brands and products for your dogs, cats, birds, fish, rabbits, guinea pigs, horses, cows, sheep, chickens and more.

For further information, please visit our web site www.kibblonest.com.au or email us directly info@kibblonest.com.au.
____
The design will be used on three different bag sizes, so our printer can reduce the design from the largest size, but please keep in mind the sizes are 280mm x 380mm, 190mm x 275mm & 160mm x 230mm.

Target Market(s)

Mostly female, 25 to 65 years of age. Pet Lovers, particuarly focussing on dogs.

Industry/Entity Type

pet industry

Requirements
Must have
• Space for sticker on front for the product name 100mm x 30mm. Also a
Nice to have
• Space for a window.
Should not have
• comical pet images. Does not need an image of a pet. Does not need an image of the food.

```html
<!DOCTYPE html>
<html lang="en">
<head>
<meta charset="utf-8">
<title>Kibblo Nest – Stand-up Pouch Artwork</title>
<link rel="stylesheet" href="https://fonts.googleapis.com/css2?family=Oswald:wght@400;500;600&family=Signika:wght@600&family=Lato:wght@400&display=swap">
<style>
  :root {
    --purple: #4b1877;
    --teal: #56bcc9;
    --teal-deep: #4fb7c6;
    --line-cyan: #2fb3c7;
    --dim-magenta: #e4137b;
    --grey: #9a9a9a;
    --white: #ffffff;
  }
  * { margin: 0; padding: 0; box-sizing: border-box; }
  html, body { width: 1200px; height: 765px; overflow: hidden; background: var(--white); }
  .artboard { position: relative; width: 1200px; height: 765px; }

  .pouch {
    position: absolute; top: 74px; width: 450px; height: 618px;
    background: linear-gradient(to bottom, #ffffff 0%, #f6fafb 38%, #c8e9ee 55%, #8dd1db 75%, var(--teal-deep) 100%);
    border: 1px solid var(--line-cyan);
  }
  .pouch--front { left: 105px; }
  .pouch--back { left: 636px; }

  .overlay { position: absolute; inset: 0; width: 1200px; height: 765px; }

  .text-abs { position: absolute; }
  .pet-food-only {
    left: 105px; width: 450px; top: 86px; text-align: center;
    font: 500 17px/1 "Oswald", sans-serif; color: var(--grey); letter-spacing: 0.5px;
  }
  .brand-name {
    font: 600 44px/1 "Oswald", sans-serif; color: var(--purple); letter-spacing: 0.3px;
    white-space: nowrap;
  }
  .brand-name--front { left: 270px; top: 205px; }
  .brand-name--back { left: 840px; top: 205px; font-size: 37px; }
  .tagline {
    font: 500 19px/1 "Oswald", sans-serif; color: var(--purple); letter-spacing: 0.4px;
    white-space: nowrap;
  }
  .tagline--front { left: 271px; top: 262px; }
  .tagline--back { left: 842px; top: 250px; font-size: 15px; }

  .web-callout {
    left: 105px; width: 450px; top: 611px; text-align: center;
    font: 600 17px/16px "Signika", sans-serif; color: var(--purple);
  }

  .info-block {
    left: 762px;
    font: 400 9.4px/11.4px "Lato", sans-serif; color: #1a1a1a;
    white-space: nowrap;
  }
  .info-block .inline-brand { font: 600 13px/1 "Oswald", sans-serif; color: var(--purple); }
  .info-owned { top: 286px; }
  .info-store { top: 342px; }
  .info-feeding { top: 466px; line-height: 11px; }
  .info-contact { top: 537px; font-size: 10px; line-height: 11.6px; }

  .storage-note {
    left: 762px; top: 579px; width: 237px; height: 18px;
    border: 2px solid var(--white);
    font: 400 6.5px/14px "Oswald", sans-serif; color: #111; text-align: center;
    white-space: nowrap; overflow: hidden;
  }
  .storage-note strong { font-weight: 600; }
</style>
</head>
<body>
<div class="artboard">

  <div class="pouch pouch--front"></div>
  <div class="pouch pouch--back"></div>

  <svg class="overlay" viewBox="0 0 1200 765">
    <g class="seal-lines" fill="none" stroke="var(--line-cyan)" stroke-width="0.8">
      <line x1="105" y1="114" x2="555" y2="114"/>
      <line x1="105" y1="122" x2="555" y2="122" stroke-dasharray="3 2"/>
      <line x1="105" y1="127" x2="555" y2="127" stroke-dasharray="3 2"/>
      <line x1="105" y1="135" x2="555" y2="135"/>
      <polyline points="105,103 110,106 105,109"/>
      <polyline points="555,103 550,106 555,109"/>

      <line x1="636" y1="114" x2="1086" y2="114"/>
      <line x1="636" y1="122" x2="1086" y2="122" stroke-dasharray="3 2"/>
      <line x1="636" y1="127" x2="1086" y2="127" stroke-dasharray="3 2"/>
      <line x1="636" y1="135" x2="1086" y2="135"/>
      <polyline points="636,103 641,106 636,109"/>
      <polyline points="1086,103 1081,106 1086,109"/>
      <line x1="652" y1="74" x2="652" y2="676" stroke-dasharray="3 2"/>
      <line x1="1070" y1="74" x2="1070" y2="676" stroke-dasharray="3 2"/>
      <line x1="652" y1="676" x2="1070" y2="676" stroke-dasharray="3 2"/>
      <line x1="636" y1="604" x2="1086" y2="604"/>
      <path d="M652 604 Q861 700 1070 604" stroke-dasharray="3 2"/>
    </g>

    <g class="brand-marks" fill="none" stroke="var(--teal)" stroke-width="3">
      <circle cx="212" cy="228" r="50"/>
      <circle cx="800" cy="219" r="35"/>
    </g>

    <path class="product-window" d="M163 425 Q166 408 200 404 Q330 380 460 404 Q494 410 495 428 L495 500 Q490 518 440 525 Q330 548 220 525 Q168 516 163 500 Z"
          fill="var(--white)" stroke="var(--line-cyan)" stroke-width="0.8" stroke-dasharray="2.5 1.5"/>

    <circle class="origin-badge" cx="458" cy="564" r="31" fill="var(--purple)" role="img" aria-label="Australian made and owned badge"/>
    <circle cx="458" cy="564" r="24" fill="var(--white)"/>

    <g class="icon-badges" fill="none" stroke="var(--purple)" stroke-width="2.6" stroke-linecap="round" stroke-linejoin="round">
      <circle cx="735" cy="307" r="17"/>
      <polyline points="727,307 733,313 744,300"/>
      <circle cx="735" cy="352" r="17"/>
      <path d="M725 345 L728 345 L731 357 L742 357 L744 348 L729 348" stroke-width="2"/>
      <circle cx="732" cy="361" r="1.4" fill="var(--purple)" stroke="none"/>
      <circle cx="741" cy="361" r="1.4" fill="var(--purple)" stroke="none"/>
      <circle cx="735" cy="494" r="17"/>
      <ellipse cx="735" cy="491" rx="9" ry="4" stroke-width="2"/>
      <path d="M726 491 L727 498 Q735 502 743 498 L744 491" stroke-width="2"/>
      <circle cx="735" cy="555" r="17"/>
      <circle cx="735" cy="555" r="9" stroke-width="1.8"/>
      <ellipse cx="735" cy="555" rx="4" ry="9" stroke-width="1.6"/>
      <line x1="726" y1="555" x2="744" y2="555" stroke-width="1.6"/>
    </g>

    <g class="dimensions" stroke="var(--dim-magenta)" stroke-width="0.7" fill="none">
      <line x1="105" y1="56" x2="105" y2="68"/><line x1="554" y1="56" x2="554" y2="68"/>
      <line x1="106" y1="63" x2="553" y2="63"/>
      <line x1="636" y1="56" x2="636" y2="68"/><line x1="1085" y1="56" x2="1085" y2="68"/>
      <line x1="637" y1="63" x2="1084" y2="63"/>
      <line x1="86" y1="74" x2="102" y2="74"/><line x1="86" y1="692" x2="102" y2="692"/>
      <line x1="94" y1="75" x2="94" y2="691"/>
      <line x1="618" y1="74" x2="634" y2="74"/><line x1="618" y1="692" x2="634" y2="692"/>
      <line x1="626" y1="75" x2="626" y2="691"/>
      <line x1="556" y1="74" x2="570" y2="74"/><line x1="556" y1="106" x2="570" y2="106"/>
      <line x1="562" y1="75" x2="562" y2="105"/>
      <line x1="572" y1="74" x2="584" y2="74"/><line x1="572" y1="114" x2="584" y2="114"/>
      <line x1="578" y1="75" x2="578" y2="113"/>
      <line x1="1088" y1="74" x2="1102" y2="74"/><line x1="1088" y1="106" x2="1102" y2="106"/>
      <line x1="1094" y1="75" x2="1094" y2="105"/>
      <line x1="1104" y1="74" x2="1116" y2="74"/><line x1="1104" y1="114" x2="1116" y2="114"/>
      <line x1="1110" y1="75" x2="1110" y2="113"/>
      <line x1="556" y1="604" x2="572" y2="604"/><line x1="556" y1="692" x2="572" y2="692"/>
      <line x1="565" y1="605" x2="565" y2="691"/>
      <line x1="1088" y1="604" x2="1104" y2="604"/><line x1="1088" y1="692" x2="1104" y2="692"/>
      <line x1="1097" y1="605" x2="1097" y2="691"/>
      <line x1="105" y1="695" x2="105" y2="704"/><line x1="121" y1="695" x2="121" y2="704"/>
      <line x1="106" y1="699" x2="120" y2="699"/>
      <line x1="538" y1="695" x2="538" y2="704"/><line x1="554" y1="695" x2="554" y2="704"/>
      <line x1="539" y1="699" x2="553" y2="699"/>
      <line x1="636" y1="695" x2="636" y2="704"/><line x1="652" y1="695" x2="652" y2="704"/>
      <line x1="637" y1="699" x2="651" y2="699"/>
      <line x1="1069" y1="695" x2="1069" y2="704"/><line x1="1085" y1="695" x2="1085" y2="704"/>
      <line x1="1070" y1="699" x2="1084" y2="699"/>
      <line x1="166" y1="376" x2="166" y2="392"/><line x1="493" y1="376" x2="493" y2="392"/>
      <line x1="167" y1="384" x2="492" y2="384"/>
      <line x1="329" y1="391" x2="329" y2="535"/>
      <line x1="329" y1="538" x2="329" y2="691"/>
    </g>
    <g class="dimension-labels" fill="var(--dim-magenta)" font-family="Arial, Helvetica, sans-serif" font-size="6.5">
      <text x="334" y="61" text-anchor="middle">280mm</text>
      <text x="866" y="61" text-anchor="middle">280mm</text>
      <text x="329" y="381" text-anchor="middle">207.14 mm</text>
      <text x="105" y="709">10mm</text><text x="538" y="709">10mm</text>
      <text x="636" y="709">10mm</text><text x="1069" y="709">10mm</text>
      <text transform="translate(92 366) rotate(-90)" text-anchor="middle">385mm</text>
      <text transform="translate(624 366) rotate(-90)" text-anchor="middle">385mm</text>
      <text transform="translate(338 462) rotate(-90)" text-anchor="middle">91.22 mm</text>
      <text transform="translate(573 652) rotate(-90)" text-anchor="middle">55mm</text>
      <text transform="translate(1105 652) rotate(-90)" text-anchor="middle">55mm</text>
      <text transform="translate(568 90) rotate(-90)" text-anchor="middle" font-size="4.5">20mm</text>
      <text transform="translate(584 93) rotate(-90)" text-anchor="middle" font-size="4.5">25mm</text>
      <text transform="translate(1100 90) rotate(-90)" text-anchor="middle" font-size="4.5">20mm</text>
      <text transform="translate(1116 93) rotate(-90)" text-anchor="middle" font-size="4.5">25mm</text>
    </g>
  </svg>

  <div class="text-abs pet-food-only">PET FOOD ONLY</div>

  <div class="text-abs brand-name brand-name--front">Kibblo Nest</div>
  <div class="text-abs tagline tagline--front">100% NATURAL PET TREATS</div>

  <div class="text-abs web-callout">Visit our web site for more products<br>www.kibblonest.com.au</div>

  <div class="text-abs brand-name brand-name--back">Kibblo Nest</div>
  <div class="text-abs tagline tagline--back">100% NATURAL PET TREATS</div>

  <p class="text-abs info-block info-owned"><span class="inline-brand">Kibblo Nest</span> is proudly Australian owned.<br>Our treats are sustainably sourced using human grade<br>ingredients from reputable Australian suppliers.</p>

  <p class="text-abs info-block info-store">Kibblo Nest products can be purchased at any time<br>through our online store.</p>

  <p class="text-abs info-block info-feeding">This product is intended as a daily treat and suitable for<br>dogs of all breeds, ages, sizes and activity levels.<br>Always select a treat suitable for your dogs individual needs.<br>Ensure fresh clean drinking water is available at all times<br>and alway supervise your pet when feeding treats.</p>

  <p class="text-abs info-block info-contact">For further information,<br>please visit our website www.kibblonest.com.au<br>or contact us at info@kibblonest.com.au.</p>

  <div class="text-abs storage-note"><strong>Storage:</strong> For optimal freshness, seal bag well and store in a cool dry and dark location.</div>

</div>
</body>
</html>
```